Vorlage für ein Workbook
Zielgruppe
Coaching und Beratung
Aufgabenstellung
Es soll eine Vorlage für ein Workbook erstellt werden, das ich dann selbst mit Inhalten füllen kann.. evtl. mit Canvas oder wie auch immer....
Es ist ein 12 Wochenkurs, d.h. ich brauche 1 Titelseite für jede Woche, die ich dann paste und copy machen kann und beschriften kann, sowie eine Vorlage für die einzelnen Seiten des Workbooks. Das Workbook in pdf Format muss auch online ausgefüllt werden können.
Design angepasst an Landingpage

```html
<!DOCTYPE html>
<html lang="de">
<head>
<meta charset="utf-8">
<title>Wellness Workbook – Vorlage</title>
<link rel="stylesheet" href="https://fonts.googleapis.com/css2?family=Cinzel:wght@400;600&family=Cormorant+Garamond:wght@400&family=Source+Sans+3:wght@400&family=Great+Vibes&display=swap">
<style>
  :root {
    --bg: #c4c4c4;
    --paper: #efefef;
    --paper-shade: #e6e6e6;
    --ink: #1e1e1e;
    --taupe: #908b85;
    --field: #d3d1ce;
    --square: #dcdbd9;
    --script: #9a958f;
    --leaf: #8fbf8a;
    --pot: #c9c9c7;
  }
  * { box-sizing: border-box; margin: 0; padding: 0; }
  html, body { width: 1200px; height: 800px; overflow: hidden; }
  body { background: var(--bg); position: relative; font-family: "Source Sans 3", sans-serif; color: var(--ink); }

  .page {
    position: absolute; top: 140px; width: 340px; height: 520px;
    background: var(--paper); overflow: hidden;
    box-shadow: 0 6px 18px rgba(0,0,0,0.12);
  }
  .page--left { left: 70px; background: linear-gradient(90deg, var(--paper) 80%, var(--paper-shade)); }
  .page--right { left: 410px; background: linear-gradient(90deg, var(--paper-shade), var(--paper) 20%); }
  .cover { left: 790px; background: var(--paper); }

  .page-number {
    position: absolute; top: 14px; right: 26px;
    font-family: "Cormorant Garamond", serif; font-size: 38px; color: var(--taupe); line-height: 1;
    font-variant-numeric: lining-nums;
  }
  .page-title {
    position: absolute; top: 58px; left: 26px;
    font-family: "Cinzel", serif; font-size: 13px; font-weight: 400;
  }
  .page-intro {
    position: absolute; top: 78px; left: 26px; width: 220px;
    font-size: 6px; line-height: 1.4;
  }
  .fields { position: absolute; top: 114px; left: 26px; right: 26px; }
  .field-label { font-family: "Cinzel", serif; font-size: 8.5px; line-height: 10px; margin-bottom: 5px; }
  .field-box { height: 60px; background: var(--field); margin-bottom: 10px; }
  .page-motto {
    position: absolute; bottom: 16px; left: 26px;
    font-family: "Great Vibes", cursive; font-size: 19px; line-height: 1; color: var(--script);
  }
  .page-plant {
    position: absolute; right: 0; bottom: 0; width: 80px; height: 52px;
    background: linear-gradient(180deg, rgba(143,191,138,0.55), rgba(210,210,208,0.7));
    opacity: 0.7;
  }

  .cover-kicker {
    position: absolute; top: 44px; left: 34px;
    font-family: "Cinzel", serif; font-weight: 600; font-size: 10px;
  }
  .cover-title {
    position: absolute; top: 60px; left: 34px; width: 280px;
    font-family: "Cinzel", serif; font-weight: 400; font-size: 21px; line-height: 1.15;
  }
  .cover-square { position: absolute; top: 150px; right: 40px; width: 34px; height: 34px; background: var(--square); }
  .cover-photo {
    position: absolute; top: 215px; left: 70px; width: 230px; height: 225px;
    background: linear-gradient(180deg, var(--paper) 0%, var(--leaf) 30%, var(--pot) 55%, #bdbdbb 100%);
  }
  .cover-band-v { position: absolute; top: 330px; left: 0; width: 24px; height: 165px; background: var(--taupe); }
  .cover-band-box {
    position: absolute; top: 440px; left: 0; width: 118px; height: 55px; background: var(--taupe);
    display: flex; align-items: center; justify-content: center;
    font-family: "Cinzel", serif; font-size: 13px; color: #f3f2f0;
  }
  .cover-foot { position: absolute; top: 440px; left: 118px; right: 0; height: 55px; background: var(--paper); }
  .cover-brand {
    position: absolute; top: 460px; left: 150px;
    display: flex; align-items: center; gap: 6px;
    font-family: "Cinzel", serif; font-size: 11px; color: var(--taupe);
  }
  .cover-brand-dot { width: 6px; height: 6px; border-radius: 50%; background: var(--taupe); }
</style>
</head>
<body>
  <section class="page page--left">
    <div class="page-number">01</div>
    <h2 class="page-title">Lorem ipsum</h2>
    <p class="page-intro">Lorem ipsum dolor sit amet, consectetur adipisci elit, sed eiusmod tempor incidunt ut labore et dolore magna aliqua. Ut enim ad minim veniam, quis nostrum exercitationem ullam corporis suscipit laboriosam,</p>
    <div class="fields">
      <div class="field-label">Lorem ipsum</div><div class="field-box"></div>
      <div class="field-label">Lorem ipsum</div><div class="field-box"></div>
      <div class="field-label">Lorem ipsum</div><div class="field-box"></div>
      <div class="field-label">Lorem ipsum</div><div class="field-box"></div>
    </div>
    <div class="page-plant" role="img" aria-label="Blasses Foto einer Sukkulente im Betontopf"></div>
    <div class="page-motto">Be The Best of You</div>
  </section>

  <section class="page page--right">
    <div class="page-number">02</div>
    <h2 class="page-title">Lorem ipsum</h2>
    <p class="page-intro">Lorem ipsum dolor sit amet, consectetur adipisci elit, sed eiusmod tempor incidunt ut labore et dolore magna aliqua. Ut enim ad minim veniam, quis nostrum exercitationem ullam corporis suscipit laboriosam,</p>
    <div class="fields">
      <div class="field-label">Lorem ipsum</div><div class="field-box"></div>
      <div class="field-label">Lorem ipsum</div><div class="field-box"></div>
      <div class="field-label">Lorem ipsum</div><div class="field-box"></div>
      <div class="field-label">Lorem ipsum</div><div class="field-box"></div>
    </div>
    <div class="page-motto">Be The Best of You</div>
  </section>

  <section class="page cover">
    <div class="cover-kicker">Wellness Workbook</div>
    <h1 class="cover-title">LOREM IPSUM DOLOR SIT AMET LOREM IPSUM</h1>
    <div class="cover-square"></div>
    <div class="cover-band-v"></div>
    <div class="cover-photo" role="img" aria-label="Foto einer grünen Sukkulente in einem grauen Betontopf"></div>
    <div class="cover-band-box">Woche 1</div>
    <div class="cover-foot"></div>
    <div class="cover-brand"><span class="cover-brand-dot"></span>Hanselore Rolfing</div>
  </section>
</body>
</html>
```